Roofing Company Sales Rep Business Card

Business card for sales rep to canvass and hand out to property owners/managers for free roof inspections and roof replacements.

```html
<!DOCTYPE html>
<html lang="en">
<head>
<meta charset="utf-8">
<title>Summit Ridge Roofing – Business Card</title>
<link href="https://fonts.googleapis.com/css2?family=Figtree:wght@400;600;700&display=swap" rel="stylesheet">
<style>
  :root {
    --backdrop: #dcdcdc;
    --card-black: #050607;
    --card-white: #f0f0f0;
    --band: #0a120e;
    --brand-red: #d0191f;
    --ink: #1b1b1b;
    --paper-text: #f2f2f2;
  }
  * { margin: 0; padding: 0; box-sizing: border-box; }
  html, body {
    width: 1200px; height: 1200px; overflow: hidden;
    background: var(--backdrop);
    font-family: "Figtree", sans-serif;
  }
  .canvas { position: relative; width: 1200px; height: 1200px; }
  .card {
    position: absolute; left: 233px; width: 732px; height: 418px;
    box-shadow: 0 6px 18px rgba(0,0,0,0.25);
  }
  .card-front { top: 160px; background: var(--card-black); }
  .card-back  { top: 631px; background: var(--card-white); }

  .wordmark {
    position: absolute; left: 0; right: 0;
    display: flex; align-items: center; justify-content: center; gap: 14px;
    font-weight: 700; font-size: 40px; letter-spacing: 1px;
  }
  .wordmark-mark { width: 22px; height: 22px; }
  .card-front .wordmark { top: 185px; color: var(--paper-text); }
  .card-front .wordmark-mark { background: var(--paper-text); }
  .card-back .wordmark { top: 118px; color: var(--ink); }
  .card-back .wordmark-mark { background: var(--brand-red); }

  .rep {
    position: absolute; right: 420px; top: 252px; text-align: right;
  }
  .rep-name { color: var(--brand-red); font-weight: 700; font-size: 31px; line-height: 1.1; }
  .rep-title { color: var(--ink); font-size: 19px; margin-top: 8px; }
  .divider {
    position: absolute; left: 342px; top: 256px; width: 2px; height: 66px; background: var(--ink);
  }
  .contacts {
    position: absolute; left: 375px; top: 250px; list-style: none;
    color: var(--ink); font-size: 19px;
  }
  .contacts li { display: flex; align-items: center; gap: 10px; height: 28px; }
  .contacts svg { width: 16px; height: 16px; flex: none; }
  .address-band {
    position: absolute; left: 0; bottom: 0; width: 100%; height: 58px;
    background: var(--band); color: var(--paper-text);
    display: flex; align-items: center; justify-content: center;
    font-size: 19px;
  }
</style>
</head>
<body>
<div class="canvas">
  <section class="card card-front">
    <div class="wordmark"><span class="wordmark-mark"></span>Summit Ridge Roofing</div>
  </section>

  <section class="card card-back">
    <div class="wordmark"><span class="wordmark-mark"></span>Summit Ridge Roofing</div>

    <div class="rep">
      <div class="rep-name">Dalton Reyes</div>
      <div class="rep-title">sales representative</div>
    </div>
    <div class="divider"></div>

    <ul class="contacts">
      <li>
        <svg viewBox="0 0 16 16" fill="var(--brand-red)"><path d="M3.5 1.5l2.2 2.6-1.2 1.8c.9 2 2.5 3.6 4.6 4.6l1.8-1.2 2.6 2.2-1.3 2.3C7.2 13.6 2.4 8.8 1.2 2.8z"/></svg>
        (405)-555-0147
      </li>
      <li>
        <svg viewBox="0 0 16 16"><rect x="1" y="3" width="14" height="10" fill="var(--brand-red)"/><path d="M1 3l7 6 7-6" fill="none" stroke="#fff" stroke-width="1.4"/></svg>
        info@summitridgeroof.com
      </li>
      <li>
        <svg viewBox="0 0 16 16" fill="none" stroke="var(--brand-red)" stroke-width="1.5"><circle cx="8" cy="8" r="6.5" fill="var(--brand-red)"/><path d="M1.5 8h13M8 1.5c-3 3.5-3 9.5 0 13M8 1.5c3 3.5 3 9.5 0 13" stroke="#fff" stroke-width="1"/></svg>
        www.summitridgeroof.com
      </li>
    </ul>

    <div class="address-band">4718 Alder Lane Lake Harmon Maine 11408</div>
  </section>
</div>
</body>
</html>
```